Islamic App which helps to calculate, track and pay Zakat

We need an application which helps muslim people to calculate and pay Zakat - mandatory donations which muslim should pay based on his income. The application will consist of two parts (applications) - the one which is used by "payer" and another one - used by "receiver". To make a payment "payer" will scan QR-code which "receiver" will generate in his app and show to payer. "Receiver" will have option to initiate cash withdrawal once he collected required minimum for the withdrawal.
Important that "payer" side journey to make a payment should be as short as possible - imaging same as you make donation by cash - you just gave money and left, similar experience should be with app - couple-three taps to make it. For receiver side major requirement is to keep the UI/UX as simple as possible, these guys usually are not aware about online payments (roughly speaking this part of the app should be more similar to Pixora rather than to banking/financial app)
In this Figma I tried to sketch the UX for both sides (just to explain the idea): https://www.plandrafo.com/file/kq4Rt8VbnWxZp2LcMs7Ea9/Draft-basics?type=design&node-id=2741-508316&mode=design

Target Market(s)

Muslims

Industry/Entity Type

Donations

Colors
0094D4
00A9DD
6FCCEA
C7EBF8
E9F6FB
00AB8E
00BBA5
67D7C9
C6EFE9
E9F9F6

Requirements
Must have
• The application should have soul. Design should show that this application intend to help people, not just money transfer
Nice to have
• Payment should be as quick as possible, in the sketches I showed it as banknotes/coins which user need to slide-up to pay. Maybe make it similar as Zelt OS dock icons?
Should not have
• The application should not look as banking/financial app or wallet app

```html
<!DOCTYPE html>
<html lang="en">
<head>
<meta charset="utf-8">
<title>Zakat App Screens</title>
<link href="https://fonts.googleapis.com/css2?family=Jost:wght@400;500;600;700&family=Inter:wght@400;500&display=swap" rel="stylesheet">
<style>
:root{
  --brand-green:#14b01a;
  --button-top:#00cc0a;
  --button-bottom:#079c10;
  --button-dark:#0a6d10;
  --paper:#ffffff;
  --ink:#2b2b2b;
  --ink-soft:#333333;
  --key-bg:#ffffff;
  --keyboard-bg:#d4d6db;
  --key-shadow:#9fa2a8;
}
*{margin:0;padding:0;box-sizing:border-box}
html,body{width:1200px;height:697px;overflow:hidden;background:var(--paper)}
.canvas{position:relative;width:1200px;height:697px;background:var(--paper);font-family:'Jost',sans-serif}
.band{position:absolute;inset:0}
.screen{position:absolute;top:83px;width:254px;height:530px;overflow:hidden;box-shadow:0 6px 18px rgba(0,0,0,.28)}
.screen--signin{left:128px}
.screen--code{left:473px}
.screen--profile{left:818px;background:var(--paper)}
.screen__backdrop{position:absolute;inset:0;background:linear-gradient(180deg,#24bd26 0%,#5cc451 30%,#a5cf82 60%,#dcdcb4 85%,#e4e2c6 100%)}
.app-title{position:absolute;top:46px;left:0;width:100%;text-align:center;color:#fff;font-weight:600;font-size:60px;letter-spacing:2px;line-height:1}
.screen-heading{position:absolute;left:0;width:100%;text-align:center;color:#fff;font-weight:600;font-size:23px;line-height:27px}
.screen-note{position:absolute;left:10px;right:10px;text-align:center;color:#fff;font-size:13px;line-height:19px;letter-spacing:.3px}
.field{position:absolute;top:234px}
.field__label{font-size:9.5px;line-height:12px;color:var(--ink-soft);letter-spacing:.1px;white-space:nowrap}
.field__value{margin-top:4px;font-size:11px;line-height:13px;font-weight:600;color:#111;letter-spacing:.4px;padding-bottom:5px;border-bottom:1px solid #444;display:flex;justify-content:space-between;align-items:center;white-space:nowrap}
.field--country{left:15px;width:56px}
.field--mobile{left:95px;width:146px}
.hint{position:absolute;top:283px;left:0;width:100%;text-align:center;font-size:12px;line-height:15px;color:#222;letter-spacing:.3px}
.action-button{position:absolute;top:312px;left:19px;width:215px;height:35px;border-radius:3px;background:linear-gradient(180deg,var(--button-top),var(--button-bottom));color:#fff;font-weight:600;font-size:11px;display:flex;align-items:center;justify-content:center;letter-spacing:.3px}
.code-slots{position:absolute;top:240px;left:0;width:100%;display:flex;justify-content:center;gap:14px}
.code-slot{width:35px;height:35px;border-radius:50%;background:#fff;border:1px solid #333}
.keypad{position:absolute;left:0;top:381px;width:254px;height:149px;background:var(--keyboard-bg);font-family:'Inter',sans-serif}
.key{position:absolute;width:81px;height:32px;background:var(--key-bg);border-radius:4px;box-shadow:0 1px 0 var(--key-shadow);text-align:center;color:#111}
.key__digit{display:block;font-size:16px;line-height:18px;padding-top:2px}
.key__letters{display:block;font-size:6px;letter-spacing:.5px;line-height:8px}
.key--zero .key__digit{padding-top:7px}
.key--delete{background:none;box-shadow:none;display:flex;align-items:center;justify-content:center}
.c1{left:1px}.c2{left:86px}.c3{left:171px}
.r1{top:2px}.r2{top:38px}.r3{top:75px}.r4{top:112px}
.profile-photo{position:absolute;inset:0;background:linear-gradient(180deg,#6b665e 0%,#8a7a66 30%,#a08c74 55%,#c9bfb2 72%,#f2f0ec 82%,#ffffff 90%)}
.icon-button{position:absolute;top:22px;width:33px;height:30px;background:#fff;border-radius:3px;display:flex;align-items:center;justify-content:center}
.icon-button--back{left:12px}
.icon-button--edit{left:209px}
.profile-name{position:absolute;top:380px;left:0;width:100%;text-align:center;font-weight:600;font-size:46px;color:var(--ink);letter-spacing:2px;line-height:1}
.profile-bio{position:absolute;top:436px;left:0;width:100%;text-align:center;font-size:13px;color:var(--ink);letter-spacing:.4px}
.pay-button{position:absolute;top:470px;left:19px;width:215px;height:35px;border-radius:3px;background:linear-gradient(180deg,var(--button-top),var(--button-bottom));display:flex;overflow:hidden}
.pay-button__amount{flex:1;display:flex;align-items:center;justify-content:center;color:#fff;font-weight:600;font-size:22px;gap:5px}
.pay-button__currency{font-size:13px}
.pay-button__icon{width:39px;background:var(--button-dark);display:flex;align-items:center;justify-content:center}
</style>
</head>
<body>
<div class="canvas">
  <svg class="band" width="1200" height="697" viewBox="0 0 1200 697" aria-hidden="true">
    <polygon points="976,0 1200,0 1200,100 214,697 0,697 0,593" fill="var(--brand-green)"/>
  </svg>

  <section class="screen screen--signin">
    <div class="screen__backdrop" role="img" aria-label="Faded photo of a smiling child in an embroidered cap under a green tint"></div>
    <h1 class="app-title">Zakat</h1>
    <h2 class="screen-heading" style="top:144px">Sign in to Zakat<br>App</h2>
    <div class="field field--country">
      <div class="field__label">Country Code</div>
      <div class="field__value"><span>+971</span>
        <svg width="7" height="5" viewBox="0 0 7 5"><path d="M1 1l2.5 2.5L6 1" stroke="#111" stroke-width="1" fill="none"/></svg>
      </div>
    </div>
    <div class="field field--mobile">
      <div class="field__label">Mobile Number</div>
      <div class="field__value"><span>888 888 8888</span></div>
    </div>
    <p class="hint">Please enter your UAE phone number</p>
    <div class="action-button">NEXT</div>
    <div class="keypad">
      <div class="key c1 r1"><span class="key__digit">1</span></div>
      <div class="key c2 r1"><span class="key__digit">2</span><span class="key__letters">ABC</span></div>
      <div class="key c3 r1"><span class="key__digit">3</span><span class="key__letters">DEF</span></div>
      <div class="key c1 r2"><span class="key__digit">4</span><span class="key__letters">GHI</span></div>
      <div class="key c2 r2"><span class="key__digit">5</span><span class="key__letters">JKL</span></div>
      <div class="key c3 r2"><span class="key__digit">6</span><span class="key__letters">MNO</span></div>
      <div class="key c1 r3"><span class="key__digit">7</span><span class="key__letters">PQRS</span></div>
      <div class="key c2 r3"><span class="key__digit">8</span><span class="key__letters">TUV</span></div>
      <div class="key c3 r3"><span class="key__digit">9</span><span class="key__letters">WXYZ</span></div>
      <div class="key key--zero c2 r4"><span class="key__digit">0</span></div>
      <div class="key key--delete c3 r4">
        <svg width="18" height="12" viewBox="0 0 18 12"><path d="M5 1h12v10H5L1 6z" fill="none" stroke="#222" stroke-width="1"/><path d="M8 4l4 4M12 4l-4 4" stroke="#222" stroke-width="1"/></svg>
      </div>
    </div>
  </section>

  <section class="screen screen--code">
    <div class="screen__backdrop" role="img" aria-label="Faded photo of a smiling woman in a headscarf under a green tint"></div>
    <h1 class="app-title">Zakat</h1>
    <h2 class="screen-heading" style="top:137px">Input Code</h2>
    <p class="screen-note" style="top:164px">We have sent an SMS with a 4 digit code to phone +971 50 7720468</p>
    <div class="code-slots">
      <span class="code-slot"></span><span class="code-slot"></span><span class="code-slot"></span><span class="code-slot"></span>
    </div>
    <div class="action-button">SIGN IN</div>
    <div class="keypad">
      <div class="key c1 r1"><span class="key__digit">1</span></div>
      <div class="key c2 r1"><span class="key__digit">2</span><span class="key__letters">ABC</span></div>
      <div class="key c3 r1"><span class="key__digit">3</span><span class="key__letters">DEF</span></div>
      <div class="key c1 r2"><span class="key__digit">4</span><span class="key__letters">GHI</span></div>
      <div class="key c2 r2"><span class="key__digit">5</span><span class="key__letters">JKL</span></div>
      <div class="key c3 r2"><span class="key__digit">6</span><span class="key__letters">MNO</span></div>
      <div class="key c1 r3"><span class="key__digit">7</span><span class="key__letters">PQRS</span></div>
      <div class="key c2 r3"><span class="key__digit">8</span><span class="key__letters">TUV</span></div>
      <div class="key c3 r3"><span class="key__digit">9</span><span class="key__letters">WXYZ</span></div>
      <div class="key key--zero c2 r4"><span class="key__digit">0</span></div>
      <div class="key key--delete c3 r4">
        <svg width="18" height="12" viewBox="0 0 18 12"><path d="M5 1h12v10H5L1 6z" fill="none" stroke="#222" stroke-width="1"/><path d="M8 4l4 4M12 4l-4 4" stroke="#222" stroke-width="1"/></svg>
      </div>
    </div>
  </section>

  <section class="screen screen--profile">
    <div class="profile-photo" role="img" aria-label="Portrait of a father in a turban with his three children, fading into white"></div>
    <div class="icon-button icon-button--back">
      <svg width="10" height="12" viewBox="0 0 10 12"><path d="M7 2L3 6l4 4" stroke="var(--button-dark)" stroke-width="1.6" fill="none"/></svg>
    </div>
    <div class="icon-button icon-button--edit">
      <svg width="20" height="20" viewBox="0 0 20 20" fill="none" stroke="#333" stroke-width="1.3"><path d="M10 3H4a1 1 0 0 0-1 1v12a1 1 0 0 0 1 1h12a1 1 0 0 0 1-1v-6"/><path d="M15 2l3 3-8 8H7v-3z"/></svg>
    </div>
    <h1 class="profile-name">Kaamil</h1>
    <p class="profile-bio">I am from Pakistan. I have three kids.</p>
    <div class="pay-button">
      <div class="pay-button__amount">847 <span class="pay-button__currency">AED</span></div>
      <div class="pay-button__icon">
        <svg width="22" height="18" viewBox="0 0 22 18" fill="none" stroke="#fff" stroke-width="1.4"><path d="M1 2h20v4H1z"/><path d="M5 6v11h12V6"/><text x="11" y="15" text-anchor="middle" font-size="9" fill="#fff" stroke="none" font-family="Jost, sans-serif" font-weight="600">$</text></svg>
      </div>
    </div>
  </section>
</div>
</body>
</html>
```